WALKING FOOD TOURISM BUSINESS. REQUEST FOR DIGITAL BROCHURE

Our business is a walking food tourism business in and around Melbourne's central city. We are needing a e-digital brochure - to be solely used as email' marketing content, not print. Therefore PDF size needs to be appropriate/suitable. Please see attached written content required for the brochure - together with our logo. For images, I am happy for designer to use our website content (www.wanderplatekitchen.com). OR any other appropriate and creative 'foodie' or Melbourne image suitable. Many thanks:)

Target Market(s)

Premium brand travellers or local adventurous Australians.

Requirements
Must have
• Quality font and images
Nice to have
• Quality Melbourne and food images. See website - wanderplatekitchen.com
Should not have
• Too much colour. Brand is black and white, sophisticated, premium product.

```html
<!DOCTYPE html>
<html lang="en">
<head>
<meta charset="utf-8">
<title>Wanderplate Kitchen Experiences – Brochure</title>
<link rel="stylesheet" href="https://fonts.googleapis.com/css2?family=Bebas+Neue&family=Montserrat:wght@400;500;600;700&display=swap">
<style>
  :root {
    --backdrop: #ebebeb;
    --paper: #ffffff;
    --navy: #1b2a36;
    --slate: #37444f;
    --ink: #1d1f22;
    --body: #3b3f44;
    --rule: #4a4f55;
    --dot-tint: #f1f2f4;
    --pill: #d4d6d8;
    --white: #ffffff;
  }
  * { box-sizing: border-box; margin: 0; padding: 0; }
  html, body { width: 879px; height: 1200px; overflow: hidden; }
  body {
    background: var(--backdrop);
    font-family: "Montserrat", sans-serif;
    color: var(--ink);
    position: relative;
  }
  .page {
    position: absolute;
    width: 334px;
    height: 472px;
    background: var(--paper);
    box-shadow: 0 4px 14px rgba(0,0,0,0.12);
    overflow: hidden;
  }
  .page--cover { left: 78px; top: 81px; }
  .page--contact { left: 472px; top: 81px; }
  .page--about { left: 78px; top: 628px; }
  .page--experiences { left: 472px; top: 628px; }

  .dot-grid { position: absolute; background: var(--dot-tint); }
  .block { position: absolute; background: var(--slate); }
  .brand {
    position: absolute;
    font-weight: 600;
    color: var(--navy);
    display: flex;
    align-items: center;
    gap: 4px;
    line-height: 1.1;
  }
  .brand__mark { width: 7px; height: 7px; background: var(--navy); flex: none; }
  .photo { position: absolute; }
  .bracket { position: absolute; border-color: var(--rule); border-style: solid; }

  /* cover */
  .cover__title {
    position: absolute; left: 22px; top: 314px;
    font-family: "Bebas Neue", sans-serif;
    font-size: 29px; line-height: 24px; color: var(--navy); letter-spacing: 0.2px;
  }
  .cover__lead {
    position: absolute; left: 22px; top: 372px; width: 212px;
    font-size: 7.6px; font-weight: 600; line-height: 9.6px; color: var(--ink);
  }
  .cover__short-rule { position: absolute; left: 22px; top: 412px; width: 46px; height: 1.5px; background: var(--rule); }
  .cover__web { position: absolute; left: 22px; top: 445px; font-size: 7.6px; font-weight: 600; letter-spacing: 0.6px; }
  .cover__long-rule { position: absolute; left: 155px; top: 451px; width: 179px; height: 2.5px; background: var(--rule); }

  /* contact */
  .contact__band { position: absolute; left: 0; top: 355px; width: 334px; height: 84px; background: var(--navy); }
  .contact__pill {
    position: absolute; left: 60px; top: 343px; width: 216px; height: 20px;
    background: var(--pill); border-radius: 7px;
    font-weight: 600; font-size: 10.5px; color: var(--navy);
    display: flex; align-items: center; justify-content: center;
  }
  .contact__list { position: absolute; left: 36px; top: 383px; list-style: none; }
  .contact__list li {
    display: flex; align-items: center; gap: 5px;
    font-size: 7.6px; font-weight: 600; color: var(--white); height: 17px;
  }
  .contact__list svg { width: 7px; height: 7px; flex: none; }
  .policy { position: absolute; left: 175px; top: 383px; width: 140px; color: var(--white); }
  .policy__title { font-size: 7.6px; font-weight: 600; margin-bottom: 3px; }
  .policy__text { font-size: 4px; line-height: 5px; }
  .social { position: absolute; left: 175px; top: 417px; display: flex; gap: 8px; }
  .social span { display: flex; align-items: center; gap: 3px; font-size: 4.6px; font-weight: 600; color: var(--white); }
  .social i { width: 6px; height: 6px; background: var(--white); display: block; }

  /* inner pages */
  .heading { position: absolute; font-size: 10px; font-weight: 400; letter-spacing: 0.3px; color: var(--navy); }
  .heading b { font-weight: 700; }
  .heading-rule { position: absolute; width: 17px; height: 1px; background: var(--rule); }
  .copy { position: absolute; font-size: 5px; line-height: 6.7px; color: var(--body); }
  .tour { position: absolute; }
  .tour__name { font-size: 6.6px; font-weight: 600; letter-spacing: 0.2px; color: var(--navy); margin-bottom: 3px; }
  .tour__spec { font-size: 5px; font-weight: 700; line-height: 6.6px; color: var(--navy); margin-bottom: 7px; }
  .tour__body { font-size: 5px; line-height: 6.7px; color: var(--body); text-align: justify; }
  .tour__body + .tour__body { margin-top: 6.5px; }

  .footer__brand { left: 23px; top: 420px; font-size: 7px; width: 60px; }
  .footer__rule { position: absolute; left: 96px; top: 443px; width: 98px; height: 1px; background: #c9cbcd; }
  .footer__rule::before { content: ""; position: absolute; left: -2px; top: -1px; width: 3px; height: 3px; border-radius: 50%; background: var(--rule); }
  .footer__ticks { position: absolute; left: 194px; top: 432px; width: 4px; height: 12px; border-left: 1px solid #aaa; border-right: 1px solid #aaa; }
  .footer__web {
    position: absolute; left: 199px; top: 432px; width: 100px; height: 12px;
    background: var(--navy); color: var(--white);
    font-size: 6px; font-weight: 600; display: flex; align-items: center; justify-content: center;
  }
  .footer__num {
    position: absolute; left: 300px; top: 431px; width: 14px; height: 14px; border-radius: 50%;
    border: 1px solid var(--navy); background: var(--white);
    font-size: 5.5px; font-weight: 700; display: flex; align-items: center; justify-content: center;
  }
</style>
</head>
<body>

<!-- Cover -->
<section class="page page--cover">
  <div class="brand" style="left:22px; top:30px; font-size:9px; width:90px;"><span class="brand__mark"></span>Wanderplate Kitchen</div>
  <div class="block" style="left:269px; top:0; width:65px; height:110px;"></div>
  <div class="bracket" style="left:95px; top:63px; width:30px; height:28px; border-width:2px 0 0 2px;"></div>
  <div class="photo" role="img" aria-label="Plated fish dish with fresh herbs on a restaurant table" style="left:99px; top:69px; width:222px; height:225px; background:linear-gradient(160deg,#5d544c 0%,#8a7a68 35%,#b7b9bb 60%,#4a4138 100%); box-shadow:0 0 0 3px #fff, 0 2px 6px rgba(0,0,0,0.25);"></div>
  <div class="block" style="left:269px; top:69px; width:52px; height:41px; opacity:0.9;"></div>
  <div class="block" style="left:0; top:233px; width:155px; height:40px;"></div>
  <div class="dot-grid" role="img" aria-label="Dot grid ornament" style="left:23px; top:160px; width:45px; height:64px;"></div>
  <div class="dot-grid" role="img" aria-label="Dot grid ornament" style="left:260px; top:318px; width:61px; height:42px;"></div>
  <h1 class="cover__title">Wanderplate Kitchen<br>Experiences</h1>
  <p class="cover__lead">Step into the city’s layered past, its flavours and its sounds, hearing the tales that shaped Melbourne into the lively, spirited place it is today.</p>
  <div class="cover__short-rule"></div>
  <div class="photo" role="img" aria-label="Glass of white wine" style="left:268px; top:374px; width:36px; height:78px; background:linear-gradient(180deg,#e8e3d6 0%,#c9b27a 45%,#8f8a80 100%); border-radius:14px 14px 3px 3px;"></div>
  <p class="cover__web">www.wanderplatekitchen.com</p>
  <div class="cover__long-rule"></div>
</section>

<!-- Contact / back cover -->
<section class="page page--contact">
  <div class="dot-grid" role="img" aria-label="Dot grid ornament" style="left:275px; top:3px; width:37px; height:38px;"></div>
  <div class="photo" role="img" aria-label="Black and white photo of a group of guests dining at a long table in a vineyard" style="left:0; top:80px; width:334px; height:275px; background:linear-gradient(180deg,#ffffff 0%,#d8d8d8 30%,#c4c4c4 60%,#eeeeee 100%);"></div>
  <div class="brand" style="left:118px; top:295px; font-size:9px; width:100px;"><span class="brand__mark"></span>Wanderplate Kitchen</div>
  <div class="contact__band"></div>
  <div class="contact__pill">For Booking Schedule &amp; Enquiry</div>
  <ul class="contact__list">
    <li><svg viewBox="0 0 10 10"><path d="M2 1 L4 1 L4.6 3.2 L3.4 4 Q4.4 6 6 6.6 L6.8 5.4 L9 6 L9 8 Q5 9.5 1 2 Z" fill="#fff"/></svg>+61 400 000 123</li>
    <li><svg viewBox="0 0 10 10"><rect x="0.5" y="2" width="9" height="6" fill="none" stroke="#fff"/><path d="M0.5 2 L5 5.5 L9.5 2" fill="none" stroke="#fff"/></svg>info@wanderplatekitchen.com</li>
    <li><svg viewBox="0 0 10 10"><circle cx="5" cy="5" r="4.2" fill="none" stroke="#fff"/><ellipse cx="5" cy="5" rx="1.8" ry="4.2" fill="none" stroke="#fff"/><path d="M0.8 5 H9.2" stroke="#fff"/></svg>www.wanderplatekitchen.com</li>
  </ul>
  <div class="policy">
    <p class="policy__title">Cancellation &amp; Amendments</p>
    <p class="policy__text">Full refund for cancellations made more than 48 hours before the tour start time. No refund for cancellations made within 48 hours of the start time.</p>
  </div>
  <div class="social">
    <span><i></i>wanderplate.kitchen</span>
    <span><i></i>Wanderplate.Kitchen</span>
  </div>
  <div class="dot-grid" role="img" aria-label="Dot grid ornament" style="left:20px; top:453px; width:37px; height:15px;"></div>
</section>

<!-- About -->
<section class="page page--about">
  <div class="dot-grid" role="img" aria-label="Dot grid ornament" style="left:23px; top:4px; width:29px; height:29px;"></div>
  <h2 class="heading" style="left:26px; top:46px;"><b>ABOUT</b> US</h2>
  <div class="heading-rule" style="left:26px; top:62px;"></div>
  <p class="copy" style="left:26px; top:72px; width:276px;">We craft walking adventures for travellers and locals alike, each one seen through a plate of memorable food. Our tours reveal the character of the city, its people and its many cultures - pausing to sip, taste and linger at well-loved kitchens and bars while sampling their signature dishes.</p>
  <h2 class="heading" style="left:26px; top:110px;"><b>OUR</b> EXPERIENCES</h2>
  <article class="tour" style="left:26px; top:140px; width:129px;">
    <h3 class="tour__name">LANEWAY TASTING TRAIL</h3>
    <p class="tour__spec">3.5 hours / A$165 Adult / A$115 Child / Up to 8 guests</p>
    <p class="tour__body">Love good food? Can never decide where to eat, and worry you are missing the best bites the city has to offer? If that sounds like you, then this trail through hidden lanes and tucked-away cafés was made for you.</p>
    <p class="tour__body">When time is short, our Laneway Tasting Trail packs in the highlights - tasting and wandering your way through the busy heart of the city’s ever-growing food scene.</p>
  </article>
  <article class="tour" style="left:26px; top:259px; width:129px;">
    <h3 class="tour__name">NIGHT MARKET STROLL</h3>
    <p class="tour__spec">3 hours / A$115 Adult / A$75.00 Child / Up to 10 guests</p>
    <p class="tour__body">Peckish? Then come and widen your tastes as we HEAD OUT AFTER DARK through the markets. This stroll suits locals and visitors who like to roam, explore and graze across the city’s Asian street food stalls. Eat your way along the aisles – slurping fragrant noodle soups, biting into steamed buns, grilled skewers, sweet treats and more – while hearing stories of the families who arrived over the decades and the recipes they carried with them. A lovely way to find some of the city’s best-kept secrets.</p>
  </article>
  <div class="bracket" style="left:282px; top:349px; width:31px; height:28px; border-width:0 3px 3px 0;"></div>
  <div class="photo" role="img" aria-label="Historic church spire and ornate city building behind bare winter trees" style="left:176px; top:114px; width:133px; height:257px; background:linear-gradient(180deg,#3a6fc0 0%,#9fb0b8 30%,#c8c39a 55%,#7d6433 80%,#5a4a2a 100%); box-shadow:0 0 0 3px #fff, 0 2px 6px rgba(0,0,0,0.25);"></div>
  <div class="dot-grid" role="img" aria-label="Dot grid ornament" style="left:269px; top:392px; width:44px; height:30px;"></div>
  <div class="brand footer__brand"><span class="brand__mark"></span>Wanderplate Kitchen</div>
  <div class="footer__rule"></div>
  <div class="footer__ticks"></div>
  <div class="footer__web">www.wanderplatekitchen.com</div>
  <div class="footer__num">1</div>
</section>

<!-- Experiences -->
<section class="page page--experiences">
  <div class="dot-grid" role="img" aria-label="Dot grid ornament" style="left:274px; top:5px; width:28px; height:41px;"></div>
  <h2 class="heading" style="left:23px; top:36px;"><b>OUR</b> EXPERIENCES</h2>
  <div class="heading-rule" style="left:23px; top:51px;"></div>
  <article class="tour" style="left:23px; top:65px; width:130px;">
    <h3 class="tour__name">CITY STORIES WALK</h3>
    <p class="tour__spec">2.5 hours / A$95 Adult / A$55 Child / Up to 12 guests</p>
    <p class="tour__body">Spend an evening in one of the city’s liveliest, most mouth-watering dining quarters. You’ll be charmed by the warmth and welcome of local hosts as you sample house specialties from some of our favourite kitchens - matching tastes and textures at every stop - and hearing the tales that turned this town into the much-loved food destination it is today.</p>
  </article>
  <article class="tour" style="left:177px; top:64px; width:135px;">
    <h3 class="tour__name">TWILIGHT WINE &amp; PLATES</h3>
    <p class="tour__spec">3 hours / A$205 Adult / A$150 Child / Up to 8 guests</p>
    <p class="tour__body">Spend an evening in one of the city’s liveliest, most mouth-watering dining quarters. You’ll be charmed by the warmth and welcome of local hosts as you sample house specialties from some of our favourite kitchens - matching wines and small plates at every stop – and hearing the tales that turned this town into the much-loved food destination it is today.</p>
  </article>
  <article class="tour" style="left:24px; top:169px; width:288px;">
    <h3 class="tour__name">CUSTOM GROUP JOURNEYS</h3>
    <p class="tour__spec" style="margin-bottom:4px;">Up to 8 hours / Tailored itineraries</p>
    <p class="tour__body">Our custom journeys are perfect for a memorable shared outing. Discover the city’s food culture with the people you enjoy most – a team day out, a family gathering, a milestone birthday or a wedding party. Every group has its own dedicated guide. Pick any of our Wanderplate Kitchen Experiences – and adjust the length, start time and walking distance to suit. Or design something new around your tastes, theme, club or company group. Whatever you choose, your CUSTOM JOURNEY will be shaped around you.</p>
  </article>
  <div class="bracket" style="left:25px; top:248px; width:18px; height:18px; border-width:3px 0 0 3px;"></div>
  <div class="bracket" style="left:293px; top:367px; width:18px; height:18px; border-width:0 3px 3px 0;"></div>
  <div class="photo" role="img" aria-label="City riverfront with ferries moored below high-rise towers" style="left:29px; top:253px; width:278px; height:127px; background:linear-gradient(180deg,#5b8fd6 0%,#9bb5cf 30%,#8a7c6a 55%,#4e5f6e 75%,#2d4a78 100%); box-shadow:0 0 0 3px #fff, 0 2px 6px rgba(0,0,0,0.25);"></div>
  <div class="dot-grid" role="img" aria-label="Dot grid ornament" style="left:0; top:371px; width:37px; height:32px;"></div>
  <div class="brand footer__brand"><span class="brand__mark"></span>Wanderplate Kitchen</div>
  <div class="footer__rule"></div>
  <div class="footer__ticks"></div>
  <div class="footer__web">www.wanderplatekitchen.com</div>
  <div class="footer__num">2</div>
</section>

</body>
</html>
```